Invitation reopening cosmetics studio

On April 28, we will start the reopening of the cosmetically studio and brew a flyer. In the supplement: - two pictures of mine - my idea of ​​flyer presentation - various logos - brochures as thought aid - 20% to the reopening -28.04.2018 from 10.00 - 20.00 o'clock - Studio is small but charming On April 28 we will reopen the opening of the cosmetically studio start and brew a flyer. In the supplement: - two pictures of mine - my idea of ​​flyer presentation - various logos - brochures as thought aid - 20% to the reopening -28.04.2018 from 10.00 - 20.00 o'clock - Studio is small but charming On April 28 we will reopen the opening of the cosmetically studio start and brew a flyer. In the supplement: - two pictures of mine - my idea of ​​flyer presentation - various logos - brochures as thought aid - 20% for reopening - 28.04.2018 from 10.00 - 20.00 o'clock - Studio is small but charming on 28. April we will start the reopening of the cosmetically studio and brew a flyer. In the supplement: - two pictures of mine - my idea of ​​flyer presentation - various logos - brochures as thought aid - 20% to the reopening -28.04.2018 from 10.00 - 20.00 o'clock - Studio is small but charming On April 28 we will reopen the opening of the cosmetically studio start and brew a flyer. In the supplement: - two pictures of mine - my idea of ​​flyer presentation - various logos - brochures as thought aid - 20% to the reopening -28.04.2018 from 10.00 - 20.00 o'clock - Studio is small but charming On April 28 we will reopen the opening of the cosmetically studio start and brew a flyer. In the supplement: - two pictures of mine - my idea of ​​flyer presentation - various logos - brochures as thought aid - 20% for reopening - 28.04.2018 from 10.00 - 20.00 o'clock - Studio is small but charming on 28. April we will start the reopening of the cosmetically studio and brew a flyer. In the supplement: - two pictures of mine - my idea of ​​flyer presentation - various logos - brochures as thought aid - 20% to the reopening -28.04.2018 from 10.00 - 20.00 o'clock - Studio is small but charming On April 28 we will reopen the opening of the cosmetically studio start and brew a flyer. In the supplement: - two pictures of mine - my idea of ​​flyer presentation - various logos - brochures as thought aid - 20% for reopening - 28.04.2018 from 10.00 - 20.00 o'clock - Studio is small but charming Medical cosmetics facials with high quality products Quenavix body treatments Depilation Pedicure Manicure Skin Analysis Medical Cosmetics Facials with high quality products Quenavix Body Treatments Depilation

Target Market(s)

Medical Cosmetics Facials with high quality products Quenavix Body Treatments Depilation Pedicure Manicure Skin Analysis Medical Cosmetics Facials with high quality products Quenavix Body Treatments Depilation

Industry/Entity Type

Cosmetic

Font styles to use
Sans Serif

Colors
fece3e
fee18a

Requirements
Must have
• The key data simple and simple, elegant, charming,
Nice to have
• Picture of me, when, where, personal, location, picture of me, when, where, personal, location, picture of me, when, where, personal, location, picture of me, when, where, personal, location, picture of me, when, where, personal, location, picture of me, when, where, personal, location,
Should not have
• different color, too full, different color, too full, different color, too full, different color, too full, different color, too full, different color, too full, different color, too full, different color, too full, different color , too full, different color, too full, different color, too full, different color, too full, different color, too full, different color, too full, different color, too full, different color, too full, different color, too full v

```html
<!DOCTYPE html>
<html lang="de">
<head>
<meta charset="utf-8">
<title>Aurelle Medical Cosmetics – Neueröffnung</title>
<link rel="stylesheet" href="https://fonts.googleapis.com/css2?family=Work+Sans:wght@400;500;600;700&display=swap">
<style>
  :root {
    --yellow: #fece3e;
    --yellow-light: #fee18a;
    --gold: #c9a14a;
    --gold-dark: #9c7a2c;
    --ink: #2e2410;
    --ink-soft: #5a4a24;
    --rule: #b8932f;
    --stage: #e9e7e3;
    --photo-top: #c9d2cc;
    --photo-mid: #8d9590;
    --photo-navy: #1f2a4a;
  }
  * { box-sizing: border-box; margin: 0; padding: 0; }
  html, body { width: 1200px; height: 1000px; overflow: hidden; }
  body { background: var(--stage); font-family: "Work Sans", Arial, sans-serif; color: var(--ink); position: relative; }

  .flyer { position: absolute; left: 50px; top: 160px; width: 1100px; height: 680px; overflow: hidden; box-shadow: 0 10px 30px rgba(0,0,0,.18); background: var(--photo-navy); }

  .portrait { position: absolute; inset: 0; background: linear-gradient(160deg, var(--photo-top) 0%, var(--photo-mid) 45%, var(--photo-navy) 78%); }

  .panel-shape { position: absolute; left: 0; top: 0; width: 1100px; height: 680px; }

  .panel { position: absolute; left: 0; top: 0; width: 560px; height: 680px; padding: 0 40px; }

  .partners { display: flex; justify-content: space-between; align-items: center; height: 100px; padding-top: 20px; border-bottom: 1.5px solid var(--rule); }
  .partner { font-weight: 600; font-size: 19px; color: var(--ink); display: flex; align-items: center; gap: 6px; }
  .partner .dot { width: 10px; height: 10px; border-radius: 50%; background: var(--ink); }

  .subhead { margin-top: 22px; font-size: 22px; font-weight: 400; color: var(--ink-soft); }
  .headline { font-size: 50px; font-weight: 700; line-height: 1.1; letter-spacing: -0.5px; }

  .services { display: grid; grid-template-columns: 290px 200px; margin-top: 12px; font-size: 20px; color: var(--ink-soft); }
  .services ul { list-style: none; }
  .services li { line-height: 28px; }
  .services li::before { content: "• "; }
  .services .col-b { margin-top: -12px; }

  .offer { margin-top: 22px; border-top: 1.5px solid var(--rule); padding-top: 22px; }
  .offer-pct { font-size: 30px; font-weight: 700; line-height: 1; }
  .offer-pct span { font-weight: 500; }
  .offer-title { font-size: 52px; font-weight: 600; line-height: 1.1; letter-spacing: 0.5px; }
  .offer-date { font-size: 38px; font-weight: 500; line-height: 1.1; }
  .offer-date small { font-size: 20px; }
  .offer-date .time { font-size: 17px; margin-left: 12px; vertical-align: middle; }

  .footer { position: absolute; left: 40px; top: 510px; width: 500px; display: flex; gap: 30px; }
  .map { width: 220px; height: 130px; background: linear-gradient(135deg, #f2f2ef, #dcdcd8); border: 3px solid #fff; box-shadow: 2px 3px 8px rgba(0,0,0,.2); }
  .contact { padding-top: 8px; color: var(--ink-soft); }
  .contact-name { font-size: 19px; }
  .contact-role { font-size: 15px; padding-bottom: 8px; border-bottom: 1px solid var(--rule); margin-bottom: 8px; }
  .contact-line { display: flex; align-items: center; gap: 8px; font-size: 14px; font-weight: 600; line-height: 26px; }
  .contact-line svg { width: 13px; height: 13px; fill: var(--ink-soft); flex: none; }

  .brand { position: absolute; left: 630px; top: 555px; display: flex; align-items: center; gap: 18px; }
  .brand-circle { width: 86px; height: 86px; border-radius: 50%; border: 3px solid var(--gold); }
  .brand-name { font-size: 38px; font-weight: 500; color: var(--gold); line-height: 1.05; }
</style>
</head>
<body>
  <article class="flyer">
    <div class="portrait" role="img" aria-label="Portrait der Studioinhaberin in einem dunkelblauen Kleid vor hellem Hintergrund"></div>

    <svg class="panel-shape" viewBox="0 0 1100 680" aria-hidden="true">
      <defs>
        <linearGradient id="goldEdge" x1="0" y1="0" x2="1" y2="1">
          <stop offset="0" stop-color="#e6c46a"/>
          <stop offset=".5" stop-color="#a57d2b"/>
          <stop offset="1" stop-color="#e2bd5c"/>
        </linearGradient>
      </defs>
      <path d="M0,0 H620 C660,0 668,50 660,130 C645,270 585,350 592,480 C598,600 640,650 620,680 H0 Z" fill="url(#goldEdge)"/>
      <path d="M0,0 H604 C644,0 650,50 642,130 C628,270 568,350 575,480 C581,600 622,650 602,680 H0 Z" fill="var(--yellow)"/>
    </svg>

    <section class="panel">
      <div class="partners">
        <span class="partner"><span class="dot"></span>Lumera</span>
        <span class="partner">Quenavix</span>
        <span class="partner">Veloria</span>
        <span class="partner">Dermalis</span>
      </div>

      <p class="subhead">Gesichtsbehandlungen mit hochwertigen</p>
      <h1 class="headline">Medical Cosmetics</h1>

      <div class="services">
        <ul class="col-a">
          <li>Quenavix</li>
          <li>Bodybehandlungen</li>
          <li>Enthaarung</li>
        </ul>
        <ul class="col-b">
          <li>Hautanalyse</li>
          <li>Pedicure</li>
          <li>Manicure</li>
        </ul>
      </div>

      <div class="offer">
        <p class="offer-pct">20% <span>ZUR</span></p>
        <p class="offer-title">NEUERÖFFNUNG</p>
        <p class="offer-date"><small>ab</small> 28.04.2018<span class="time">VON 10.00 - 20.00 UHR</span></p>
      </div>
    </section>

    <div class="footer">
      <div class="map" role="img" aria-label="Lageplan des Studios"></div>
      <div class="contact">
        <p class="contact-name">Mirela Kostani</p>
        <p class="contact-role">Aurelle Medical Cosmetics</p>
        <p class="contact-line"><svg viewBox="0 0 24 24"><path d="M12 2a7 7 0 0 0-7 7c0 5 7 13 7 13s7-8 7-13a7 7 0 0 0-7-7zm0 9.5A2.5 2.5 0 1 1 12 6.5a2.5 2.5 0 0 1 0 5z"/></svg>Piazza 5, CH-8760 Talwil</p>
        <p class="contact-line"><svg viewBox="0 0 24 24"><path d="M6.6 10.8a15 15 0 0 0 6.6 6.6l2.2-2.2a1 1 0 0 1 1-.25 11.4 11.4 0 0 0 3.6.57 1 1 0 0 1 1 1V20a1 1 0 0 1-1 1A17 17 0 0 1 3 4a1 1 0 0 1 1-1h3.5a1 1 0 0 1 1 1c0 1.25.2 2.45.57 3.57a1 1 0 0 1-.25 1z"/></svg>079 000 12 34</p>
        <p class="contact-line"><svg viewBox="0 0 24 24"><circle cx="12" cy="12" r="10"/></svg>www.aurelle-mc.ch</p>
      </div>
    </div>

    <div class="brand">
      <span class="brand-circle"></span>
      <span class="brand-name">Aurelle<br>Medical Cosmetics</span>
    </div>
  </article>
</body>
</html>
```